TVQ-Business Card Design

I need a modern, professional business card design that includes my logo as the main feature, maybe the entire background with the contact info overlaying or even contact info on the back and the logo full frontal

Neat and organized placement of contact information

Would like to see options in black and white

Target Market(s)

real estate Developers, Construction managers, business and home owners

Industry/Entity Type

Construction

Contact Information for Business Card

TVQ Construction
Dennis Fairweather
General Contractor

Office: 1-888-902-7351 Ext #1
Cell: 412-730-2168
Fax: 1-888-902-7351

Font styles to use
Serif

Requirements
Must have
• title
• office #
• cell #
• Email
• website
Nice to have
• fax

```html
<!DOCTYPE html>
<html lang="en">
<head>
<meta charset="utf-8">
<title>TVQ Construction – Business Cards</title>
<link rel="stylesheet" href="https://fonts.googleapis.com/css2?family=Roboto:wght@300;400;700&display=swap">
<style>
  :root {
    --page-bg: #e4e6e5;
    --card-white: #ffffff;
    --card-black: #1c1c1c;
    --brand-green: #3fa533;
    --ink-grey: #4a4a4a;
    --line-silver: #bdbdbd;
    --text-light: #e9e9e9;
  }
  * { box-sizing: border-box; margin: 0; padding: 0; }
  html, body { width: 1200px; height: 1200px; overflow: hidden; }
  body {
    background: var(--page-bg);
    font-family: "Roboto", Arial, sans-serif;
    display: flex;
    flex-direction: column;
    align-items: center;
    justify-content: center;
    gap: 80px;
  }
  .card {
    width: 840px;
    height: 480px;
    border-radius: 6px;
    box-shadow: 0 10px 30px rgba(0,0,0,0.18);
    position: relative;
  }

  /* Front */
  .card-front {
    background: var(--card-white);
    display: flex;
    flex-direction: column;
    align-items: center;
    justify-content: center;
  }
  .brand-mark {
    display: flex;
    align-items: center;
    gap: 22px;
  }
  .brand-mark .mark-square {
    width: 46px; height: 46px;
    background: var(--brand-green);
  }
  .brand-mark .brand-name {
    font-size: 150px;
    font-weight: 700;
    color: var(--brand-green);
    line-height: 1;
    letter-spacing: 4px;
  }
  .brand-tagline {
    margin-top: 14px;
    font-size: 22px;
    font-weight: 700;
    letter-spacing: 4px;
    color: var(--brand-green);
    text-transform: uppercase;
  }
  .front-website {
    position: absolute;
    bottom: 34px;
    left: 0; right: 0;
    text-align: center;
    font-size: 20px;
    font-weight: 300;
    letter-spacing: 6px;
    color: var(--ink-grey);
  }

  /* Back */
  .card-back {
    background: var(--card-black);
    color: var(--text-light);
    display: flex;
    align-items: center;
    padding: 0 56px;
  }
  .identity {
    width: 330px;
  }
  .identity .brand-mark .mark-square { width: 22px; height: 22px; background: var(--text-light); }
  .identity .brand-mark { gap: 12px; margin-bottom: 34px; }
  .identity .brand-mark .brand-name { font-size: 60px; color: var(--text-light); letter-spacing: 3px; }
  .person-name {
    font-size: 38px;
    font-weight: 400;
    margin-bottom: 14px;
  }
  .person-role {
    font-size: 20px;
    font-weight: 300;
    line-height: 1.5;
    letter-spacing: 1px;
  }
  .divider {
    width: 2px;
    height: 260px;
    background: var(--line-silver);
    margin: 0 44px 0 20px;
  }
  .contact-list { list-style: none; }
  .contact-list li {
    display: flex;
    align-items: center;
    gap: 18px;
    font-size: 20px;
    font-weight: 300;
    letter-spacing: 1px;
    margin: 14px 0;
  }
  .contact-list svg { width: 28px; height: 28px; flex: none; }
  .contact-list .site { letter-spacing: 4px; }
</style>
</head>
<body>

<section class="card card-front">
  <div class="brand-mark">
    <span class="mark-square"></span>
    <span class="brand-name">TVQ</span>
  </div>
  <p class="brand-tagline">Tri-Valley Quality Homes</p>
  <p class="front-website">www.tvqconstruction.net</p>
</section>

<section class="card card-back">
  <div class="identity">
    <div class="brand-mark">
      <span class="mark-square"></span>
      <span class="brand-name">TVQ</span>
    </div>
    <h1 class="person-name">Dennis Fairweather</h1>
    <p class="person-role">TVQ Construction<br>General Contractor</p>
  </div>
  <div class="divider"></div>
  <ul class="contact-list">
    <li>
      <svg viewBox="0 0 28 28"><circle cx="14" cy="14" r="13" fill="#e9e9e9"/><rect x="7" y="9" width="14" height="10" fill="none" stroke="#1c1c1c" stroke-width="1.6"/><path d="M7 9 L14 15 L21 9" fill="none" stroke="#1c1c1c" stroke-width="1.6"/></svg>
      dennis@tvqconstruction.net
    </li>
    <li>
      <svg viewBox="0 0 28 28"><circle cx="14" cy="14" r="13" fill="#e9e9e9"/><path d="M9 8 L12 8 L13 11 L11 12.5 Q13 16 15.5 17 L17 15 L20 16 L20 19 Q13 20 9 11 Z" fill="#1c1c1c"/></svg>
      1-888-902-7351
    </li>
    <li>
      <svg viewBox="0 0 28 28"><circle cx="14" cy="14" r="13" fill="#e9e9e9"/><rect x="8" y="12" width="12" height="8" rx="1" fill="#1c1c1c"/><path d="M7 11 Q14 5 21 11" fill="none" stroke="#1c1c1c" stroke-width="2"/></svg>
      1-888-902-7351 Ext #1 (OFFICE)
    </li>
    <li>
      <svg viewBox="0 0 28 28"><circle cx="14" cy="14" r="13" fill="#e9e9e9"/><rect x="10" y="6" width="8" height="16" rx="1.5" fill="#1c1c1c"/><circle cx="14" cy="19.5" r="1" fill="#e9e9e9"/></svg>
      412-730-2168
    </li>
    <li>
      <svg viewBox="0 0 28 28"><circle cx="14" cy="14" r="13" fill="#e9e9e9"/><circle cx="14" cy="14" r="7" fill="none" stroke="#1c1c1c" stroke-width="1.5"/><ellipse cx="14" cy="14" rx="3" ry="7" fill="none" stroke="#1c1c1c" stroke-width="1.5"/><path d="M7 14 H21" stroke="#1c1c1c" stroke-width="1.5"/></svg>
      <span class="site">www.tvqconstruction.net</span>
    </li>
  </ul>
</section>

</body>
</html>
```